HIDE WARDEN

Labels for Men's Skin Care. Organic, target 25-35 The label will be 2x3.5 on a 4oz amber bottle. 3 labels with the information shown on the uploaded sample.
Our product is a e-commerce built to help my 24 year old twin sons have a business of their own. Although it will be sold online they will also do foot work and sell to barbers at barber shops using as a mist on customers after shaving. So we want something that will attract male customers and will look good in a modern Barbershop. This is there shot and packaging is very very important. So if you could help us out with a great label we would be working with you in the future for package design. Our line will have several mens Organic natural skin care cleanser, mask toners and moisturizers..Thank you for your help. We also hope to put our products in beauty supply shops. So it needs to stand out as a mans product but still be traditional male product. Oh be creative mind that you are and remember we are trying to build a brand that attracts 25-35 male. Thank you

Hello, I just wanted to let you know that I am up working very late.

for anyone on the other side of the world up and working. I sleep about
3 hours.. So I'll be up for a few more hours and then up again around 5am my time

Good morning... I just wanted to say I will need three labels.. The words on all three are not that different and will fit pretty much the same on all three. So if you could work with one showing how the colors might be a little different on the other two you can do that with just the one label Just to make it easier on you if you like.. we can fix the other two once I find the right label,  Thank you it is 3am here.. still working.. I love it.

Target Market(s)

MALE 25-35

Industry/Entity Type

E-Commerce

Requirements
Must have
• final design must be fitted to the dieline uploaded.

```html
<!DOCTYPE html>
<html lang="en">
<head>
<meta charset="utf-8">
<title>Hide Warden – Men's Label Range</title>
<link rel="stylesheet" href="https://fonts.googleapis.com/css2?family=Didact+Gothic&family=Tinos:wght@400;700&display=swap">
<style>
  :root {
    --page-bg: #f3f3f3;
    --cream-light: #e2d8b8;
    --cream-dark: #b3a079;
    --cream-ink: #3b1a0f;
    --cream-band: #5b1c12;
    --green-light: #c3d85a;
    --green-dark: #6c8a26;
    --green-ink: #1f2a0b;
    --green-band: #2d3c12;
    --gold-light: #efcf6a;
    --gold-dark: #a56f1f;
    --gold-ink: #2f1405;
    --gold-band: #5a1309;
    --band-text: #ead9b4;
  }
  * { box-sizing: border-box; margin: 0; padding: 0; }
  html, body { width: 1200px; height: 874px; overflow: hidden; }
  body {
    background: var(--page-bg);
    font-family: "Didact Gothic", "Century Gothic", sans-serif;
  }
  .label-range {
    position: absolute;
    left: 90px; top: 232px;
    display: flex; gap: 60px;
  }
  .label {
    position: relative;
    width: 300px; height: 410px;
    overflow: hidden;
    color: var(--ink);
  }
  .label--cream { --light: var(--cream-light); --dark: var(--cream-dark); --ink: var(--cream-ink); --band: var(--cream-band); }
  .label--green { --light: var(--green-light); --dark: var(--green-dark); --ink: var(--green-ink); --band: var(--green-band); }
  .label--gold  { --light: var(--gold-light);  --dark: var(--gold-dark);  --ink: var(--gold-ink);  --band: var(--gold-band); }

  .label__texture {
    position: absolute; inset: 0;
    background: radial-gradient(ellipse at 40% 35%, var(--light) 0%, var(--dark) 100%);
  }
  .label__brand {
    position: absolute; left: 0; right: 0; top: 30px;
    display: flex; align-items: center; justify-content: center; gap: 10px;
    font-size: 20px; letter-spacing: 3px;
    color: var(--band);
  }
  .label__brand-dot {
    width: 14px; height: 14px; border-radius: 50%;
    background: var(--band);
  }
  .label__rule {
    position: absolute; left: 18px; right: 0; top: 96px;
    height: 3px; background: var(--band);
  }
  .label__band {
    position: absolute; left: 18px; top: 96px;
    width: 44px; height: 290px;
    background: var(--band);
  }
  .label__title {
    position: absolute; left: 70px; top: 104px;
    font-size: 33px; line-height: 1;
    letter-spacing: -0.5px; font-weight: 400;
  }
  .label__subtitle {
    position: absolute; left: 71px; top: 137px;
    font-family: "Tinos", "Times New Roman", serif;
    font-size: 10px; letter-spacing: 0.5px;
  }
  .label__claim {
    position: absolute; left: 71px; top: 156px; width: 180px;
    font-size: 18px; line-height: 1.02;
    letter-spacing: -0.3px;
  }
  .label__strip {
    position: absolute; left: 62px; right: 0; top: 280px;
    height: 20px; background: var(--band);
    color: var(--band-text);
    font-size: 10.5px; line-height: 20px; letter-spacing: 0.6px;
    padding-left: 10px; text-transform: uppercase;
  }
  .label--gold .label__strip { right: 26px; color: var(--gold-light); font-size: 9.5px; }
  .label__detail {
    position: absolute; left: 72px; top: 308px;
    font-family: "Tinos", "Times New Roman", serif;
    font-size: 10.5px; line-height: 1.35;
  }
  .label__detail-head { text-transform: uppercase; letter-spacing: 0.3px; }
  .label__volume {
    position: absolute; left: 62px; right: 0; top: 368px;
    font-family: "Tinos", "Times New Roman", serif;
    font-size: 10px; text-align: center;
  }
</style>
</head>
<body>
<main class="label-range">

  <article class="label label--cream">
    <div class="label__texture" role="img" aria-label="Weathered parchment texture with a faint tree silhouette"></div>
    <p class="label__brand"><span class="label__brand-dot"></span>HIDE WARDEN</p>
    <div class="label__rule"></div>
    <div class="label__band"></div>
    <h2 class="label__title">Men's</h2>
    <p class="label__subtitle">DAILY BLADE RELIEF</p>
    <p class="label__claim">soothing face toner that eases razor sting post shave</p>
    <p class="label__strip">Calm skin blend</p>
    <p class="label__detail"><span class="label__detail-head">Herbal recovery mist</span><br>Cherry + Blood Orange</p>
    <p class="label__volume">3.5fl oz 103ml</p>
  </article>

  <article class="label label--green">
    <div class="label__texture" role="img" aria-label="Green grunge texture with a faint tree silhouette"></div>
    <p class="label__brand"><span class="label__brand-dot"></span>HIDE WARDEN</p>
    <div class="label__rule"></div>
    <div class="label__band"></div>
    <h2 class="label__title">Men's</h2>
    <p class="label__subtitle">DAILY BLADE RELIEF</p>
    <p class="label__claim">helps stop ingrown bumps and cools razor sting post shave</p>
    <p class="label__strip">Cool + hydrate</p>
    <p class="label__detail"><span class="label__detail-head">Herbal recovery mist</span><br>Fig Leaf + Oat Milk</p>
    <p class="label__volume">3.5fl oz 103ml</p>
  </article>

  <article class="label label--gold">
    <div class="label__texture" role="img" aria-label="Golden grunge texture with a faint tree silhouette"></div>
    <p class="label__brand"><span class="label__brand-dot"></span>HIDE WARDEN</p>
    <div class="label__rule"></div>
    <div class="label__band"></div>
    <h2 class="label__title">Undercare</h2>
    <p class="label__subtitle">REFRESHER</p>
    <p class="label__claim">keeps the groin fresh and dry while easing skin redness and rubbing</p>
    <p class="label__strip">Pure plant care</p>
    <p class="label__volume">3.5fl oz 103ml</p>
  </article>

</main>
</body>
</html>
```